Brixelo Photography Business Cards

We need a good general business card that we can hand to our clients. We will be doing embossed gloss cards.

Target Market(s)

Real estate / Business to business / professionals

```html
<!DOCTYPE html>
<html lang="en">
<head>
<meta charset="utf-8">
<title>Brixelo Photography – Business Card</title>
<link rel="stylesheet" href="https://fonts.googleapis.com/css2?family=Montserrat:wght@400;500;700&display=swap">
<style>
  :root {
    --navy: #24215e;
    --ink: #1c1c1c;
    --card: #ffffff;
    --backdrop: #e9e7e3;
  }
  * { margin: 0; padding: 0; box-sizing: border-box; }
  html, body {
    width: 1200px;
    height: 892px;
    overflow: hidden;
    background: var(--backdrop);
    font-family: "Montserrat", Arial, sans-serif;
  }
  .card {
    position: absolute;
    left: 150px;
    top: 189px;
    width: 900px;
    height: 514px;
    background: var(--card);
    box-shadow: 0 10px 30px rgba(0,0,0,.12);
  }
  .brand {
    position: absolute;
    left: 74px;
    top: 70px;
    display: flex;
    align-items: center;
    gap: 16px;
    color: var(--navy);
    font-weight: 700;
    font-size: 52px;
    letter-spacing: 0.5px;
  }
  .brand-dot {
    width: 22px;
    height: 22px;
    border-radius: 50%;
    background: var(--navy);
  }
  .person {
    position: absolute;
    left: 70px;
    top: 178px;
    color: var(--navy);
  }
  .person-name {
    font-weight: 700;
    font-size: 27px;
    letter-spacing: 0.3px;
  }
  .person-role {
    font-weight: 500;
    font-size: 24px;
    color: var(--ink);
    margin-top: 2px;
  }
  .divider {
    position: absolute;
    left: 46px;
    right: 46px;
    top: 258px;
    height: 2px;
    background: var(--navy);
  }
  .contacts {
    position: absolute;
    left: 52px;
    top: 280px;
    list-style: none;
    color: var(--ink);
    font-size: 22px;
    line-height: 1;
  }
  .contacts li {
    display: flex;
    align-items: center;
    gap: 10px;
    margin-bottom: 15px;
  }
  .contacts svg { width: 22px; height: 22px; flex: none; }
  .address {
    position: absolute;
    right: 70px;
    top: 390px;
    text-align: right;
    color: var(--ink);
    font-size: 22px;
    line-height: 1.4;
  }
</style>
</head>
<body>
  <div class="card">
    <div class="brand"><span class="brand-dot"></span>Brixelo Photography</div>

    <div class="person">
      <div class="person-name">PERSON’S NAME</div>
      <div class="person-role">DESIGNATION</div>
    </div>

    <div class="divider"></div>

    <ul class="contacts">
      <li>
        <svg viewBox="0 0 24 24" aria-hidden="true"><circle cx="12" cy="12" r="11" fill="none" stroke="#24215e" stroke-width="2"/><path d="M8.5 6.5l2 2.5-1.2 1.3a7 7 0 0 0 4.4 4.4l1.3-1.2 2.5 2-1.3 1.8c-4.5-.3-8.7-4.5-9-9z" fill="#24215e"/></svg>
        +0 123 456 789
      </li>
      <li>
        <svg viewBox="0 0 24 24" aria-hidden="true"><circle cx="12" cy="12" r="11" fill="#24215e"/><rect x="6" y="8" width="12" height="8" fill="#fff"/><path d="M6 8l6 5 6-5" fill="none" stroke="#24215e" stroke-width="1.4"/></svg>
        info@yourmail.com
      </li>
      <li>
        <svg viewBox="0 0 24 24" aria-hidden="true"><circle cx="12" cy="12" r="11" fill="#24215e"/><circle cx="12" cy="12" r="6.5" fill="none" stroke="#fff" stroke-width="1.3"/><ellipse cx="12" cy="12" rx="3" ry="6.5" fill="none" stroke="#fff" stroke-width="1.3"/><path d="M5.5 12h13" stroke="#fff" stroke-width="1.3"/></svg>
        www.yourcompany.com
      </li>
    </ul>

    <div class="address">Your address, Suit # 000,Dummy<br>Street,City, State,</div>
  </div>
</body>
</html>
```